Marlow Brochure

Brevik & Solan Education Group was formed in 2011 as an organizational arm
to put educational and charitable services together for community
development.

B & S was acquired by Marlow Education Group in 2013 and relocated to Texas
with the expressed focus of reaching underserved communities and
population, both in the Dallas- Fort Worth Metropolitan area and Houston
areas. Key members of the organization are based in Dallas, TX, Houston,
TX, Atlanta GA, and Washington DC and are strategically networked to
utilize their external resources for education advancement with
under-served populations.

Target Market(s)

- -The target market is 17-45 year olds, the demographics are 70%
women, 30% men, interested in an entry level education in
the health field

Industry/Entity Type

Education

```html
<!DOCTYPE html>
<html lang="en">
<head>
<meta charset="utf-8">
<title>Marlow Education Group – Home Health Aide</title>
<link rel="stylesheet" href="https://fonts.googleapis.com/css2?family=Arimo:wght@400;700&family=Archivo+Narrow:wght@700&family=Tinos:wght@700&display=swap">
<style>
  :root {
    --brand-blue: #0d5c91;
    --brand-green: #7dc11f;
    --brand-green-text: #8cc63f;
    --brand-lime: #c9d84a;
    --logo-grey: #5a7f96;
    --paper: #ffffff;
    --swoosh: #eceff1;
    --photo-top: #f3f1ee;
    --photo-mid: #ebe5de;
    --text-light: #ffffff;
  }
  html, body {
    margin: 0;
    padding: 0;
    width: 1200px;
    height: 928px;
    overflow: hidden;
    background: var(--paper);
  }
  .brochure {
    position: relative;
    width: 1200px;
    height: 928px;
    overflow: hidden;
    background: var(--paper);
    font-family: "Arimo", Arial, sans-serif;
  }
  .hero-photo {
    position: absolute;
    left: 0;
    top: 0;
    width: 1200px;
    height: 928px;
    background: linear-gradient(180deg, var(--photo-top) 0%, var(--photo-mid) 55%, var(--paper) 78%);
  }
  .backdrop {
    position: absolute;
    left: 0;
    top: 0;
  }
  .brand {
    position: absolute;
    left: 888px;
    top: 120px;
    display: flex;
    align-items: center;
    gap: 12px;
    font-size: 22px;
    font-weight: 400;
    color: var(--logo-grey);
    white-space: nowrap;
  }
  .brand-dot {
    width: 26px;
    height: 26px;
    border-radius: 50%;
    background: var(--logo-grey);
  }
  .tagline {
    position: absolute;
    left: 910px;
    top: 436px;
    width: 285px;
    height: 142px;
    background: var(--brand-green);
    color: var(--text-light);
    font-family: "Archivo Narrow", "Arial Narrow", sans-serif;
    font-weight: 700;
    text-align: center;
    line-height: 1;
    padding-top: 12px;
    box-sizing: border-box;
  }
  .tagline-lead { display: block; font-size: 40px; }
  .tagline-mid { display: block; font-size: 23px; margin-top: 10px; }
  .tagline-end { display: block; font-size: 32px; margin-top: 6px; }
  .program-title {
    position: absolute;
    left: 86px;
    top: 460px;
    margin: 0;
    font-family: "Tinos", "Times New Roman", serif;
    font-weight: 700;
    font-size: 25px;
    color: var(--brand-green-text);
  }
  .program-copy {
    position: absolute;
    left: 56px;
    top: 520px;
    width: 520px;
    color: var(--text-light);
    font-size: 14.5px;
    line-height: 21px;
  }
  .program-copy p { margin: 0 0 21px; }
  .contact {
    position: absolute;
    left: 202px;
    top: 836px;
    font-weight: 700;
    font-size: 18px;
    line-height: 26px;
    color: var(--brand-lime);
    text-align: center;
  }
  .contact span { display: block; }
  .site-link {
    position: absolute;
    left: 808px;
    top: 864px;
    font-size: 20px;
    color: var(--brand-green-text);
  }
</style>
</head>
<body>
<main class="brochure">
  <div class="hero-photo" role="img" aria-label="Photograph of a cheerful group of men and women of different ages jumping in the air with raised arms on a white background"></div>

  <svg class="backdrop" width="1200" height="928" viewBox="0 0 1200 928" aria-hidden="true">
    <path class="swoosh" d="M620,640 C820,668 1020,690 1200,672 L1200,812 C960,806 800,740 620,640 Z" fill="var(--swoosh)" opacity="0.8"/>
    <path class="wave-accent" d="M0,418 C150,376 330,370 520,490 C720,620 900,796 1200,806 L1200,928 L0,928 Z" fill="var(--brand-green)"/>
    <path class="wave-panel" d="M0,430 C150,388 330,382 520,502 C720,632 900,808 1200,818 L1200,928 L0,928 Z" fill="var(--brand-blue)"/>
    <rect class="base-band" x="0" y="906" width="1200" height="22" fill="var(--brand-green)"/>
  </svg>

  <div class="brand">
    <span class="brand-dot"></span>
    <span class="brand-name">Marlow Education Group</span>
  </div>

  <div class="tagline">
    <span class="tagline-lead">Connecting</span>
    <span class="tagline-mid">Your Training To</span>
    <span class="tagline-end">Your Purpose…</span>
  </div>

  <h1 class="program-title">Home Health Aide</h1>

  <div class="program-copy">
    <p>As home health care becomes more and more prominent,<br>
    there is a growing need for Certified Home Health Aid<br>
    Certified Home Health Aides are a very important piece of the<br>
    Health Care Industry.&nbsp; Caring for a patient in their home can be<br>
    difficult and challenging, but at the same time can be fun and<br>
    rewarding.&nbsp; A successful HHA needs to possess unique skills that many<br>
    other health care providers may not.</p>
    <p>At Marlow Education Group we currently offer a Home Health Aide<br>
    Certification Program that develops the skills necessary for success in the<br>
    health care industry.</p>
  </div>

  <div class="contact">
    <span class="contact-web">www.MarlowLearn.com</span>
    <span class="contact-phone">555.014.2286</span>
  </div>

  <div class="site-link">www.MarlowLearn.com</div>
</main>
</body>
</html>
```